Killer Webpage Design

I currently have a self-hosted webpage through wordpress at www.vantrelmedia.com - the content is complete and I'm happy with this but I need it designed (no coding) to complete my requirements. I'm happy to take designs which are non-Wordpress if there is specific advantage in this.

My full branding logos are attached along with color files. My main aim is consistent branding across all areas (social media, business cards, emails, websites). I have the rest running but am not happy with the available default selections from Wordpress.

I would prefer to use the darker blue version of the logo as I feel this has more standout in online media, however I would appreciate submissions with both variants to help me choose.

With the homepage I will also want to see blog pages and category pages designed but this can come after I have selected a design to go with,

Sites that I like and are related to my business include the following:
http://www.plumora.com/au/accounting-software/
http://www.taskgriddle.com/home.aspx
https://brimtill.com/register
Updates

Apologies for the confusion - to clarify for designers I am looking for design only, no coding.

FYI - i have now uploaded business cards for an idea of the contemporary style of design completed so far.

Target Market(s)

small to medium business. Not systemised but looking for help and support.

Industry/Entity Type

Business

Requirements
Must have
• I'm looking for a minimalist professional page, with the ability to easily add new sections when required. I will also need a CMS to add blog posts on the go, with the same features that it currently has (comments, social logon etc)

```html
<!DOCTYPE html>
<html lang="en">
<head>
<meta charset="utf-8">
<title>Vantrel Media – Specialist Business Consultants</title>
<link href="https://fonts.googleapis.com/css2?family=Fjalla+One&family=Yanone+Kaffeesatz:wght@300;400&family=Open+Sans:wght@400;600;700&display=swap" rel="stylesheet">
<style>
:root{
  --navy:#0b2a3a;
  --navy-deep:#082130;
  --nav-band:#0d4a5c;
  --teal:#1fc4cf;
  --teal-bright:#27d3de;
  --teal-dark:#0f8f9a;
  --ink:#111d24;
  --body:#1b1b1b;
  --muted:#6f7a80;
  --rule:#d8dde0;
  --foot:#2c2e31;
  --foot-deep:#1d1e20;
  --foot-text:#b9bec2;
  --white:#ffffff;
}
*{box-sizing:border-box;margin:0;padding:0}
html,body{width:1038px;height:1200px;overflow:hidden}
body{position:relative;background:var(--white);font-family:Arial,Helvetica,sans-serif;color:var(--body)}

/* header */
.site-header{position:absolute;left:0;top:0;width:1038px;height:90px;background:var(--navy);border-top:2px solid var(--teal)}
.brand{position:absolute;left:126px;top:14px;display:flex;align-items:center;gap:12px}
.brand-dot{width:58px;height:58px;border-radius:50%;background:var(--teal)}
.brand-name{font-family:'Open Sans',sans-serif;font-weight:700;font-size:32px;color:var(--white);line-height:1}
.brand-tag{font-family:'Open Sans',sans-serif;font-size:14px;color:var(--white);margin-top:4px}
.call{position:absolute;right:101px;top:10px;font-family:'Yanone Kaffeesatz',sans-serif;font-size:25px;color:var(--teal-bright)}
.call span{color:var(--white)}
.search{position:absolute;left:755px;top:48px;width:183px;height:21px;background:var(--white);font-size:11px;padding:4px 8px;color:#222}
.search svg{position:absolute;right:6px;top:3px}

.main-nav{position:absolute;left:0;top:90px;width:1038px;height:38px;background:var(--nav-band);border-top:2px solid #1a8a98;border-bottom:2px solid var(--white)}
.main-nav ul{list-style:none;display:flex;gap:30px;position:absolute;left:116px;top:4px}
.main-nav a{font-family:'Yanone Kaffeesatz',sans-serif;font-size:21px;color:var(--white);text-decoration:none}

/* hero */
.hero{position:absolute;left:0;top:128px;width:1038px;height:354px;background:linear-gradient(#1dc0cc,#25cad6);border-bottom:3px solid #e9f2f3;overflow:hidden}
.hero-title{position:absolute;left:122px;top:22px;font-family:'Fjalla One',sans-serif;font-size:48px;color:var(--navy);letter-spacing:1px}
.hero-sub{position:absolute;left:124px;top:88px;font-family:'Yanone Kaffeesatz',sans-serif;font-size:24px;color:var(--white)}
.hero-copy{position:absolute;left:124px;top:118px;font-family:'Yanone Kaffeesatz',sans-serif;font-weight:300;font-size:23px;line-height:29px;color:var(--navy);white-space:nowrap}
.hero-cta{position:absolute;left:122px;top:232px;font-family:'Fjalla One',sans-serif;font-size:24px;color:var(--navy)}
.consult{position:absolute;left:124px;top:282px;width:150px;height:72px;text-decoration:none}
.consult svg{position:absolute;left:0;top:0}
.consult-small{position:absolute;left:40px;top:11px;width:80px;text-align:center;font-size:12px;line-height:14px;color:#111}
.consult-big{position:absolute;left:0;top:44px;width:150px;text-align:center;font-family:'Yanone Kaffeesatz',sans-serif;font-size:21px;line-height:24px;color:var(--navy);white-space:nowrap}
.hero-art{position:absolute;left:565px;top:10px;width:375px;height:330px;border-radius:170px 170px 30px 30px;background:radial-gradient(ellipse at 55% 40%,#ffffff 0%,#d8f4f6 45%,#3ccad4 100%)}

/* content */
.content{position:absolute;left:0;top:485px;width:1038px;height:475px;background:linear-gradient(#f1f3f4,#ffffff 90px)}
.col-main{position:absolute;left:100px;top:20px;width:568px}
.col-side{position:absolute;left:700px;top:22px;width:230px}
.col-divider{position:absolute;left:680px;top:22px;width:1px;height:428px;background:var(--rule)}
h1.welcome{font-family:'Fjalla One',sans-serif;font-weight:400;font-size:28px;color:var(--ink);margin-bottom:8px}
.col-main p{font-size:11px;line-height:14.5px;margin-bottom:14px}
.section-rule{height:1px;background:var(--rule);width:552px;margin:10px 0 16px}
h2.section{font-family:'Fjalla One',sans-serif;font-weight:400;font-size:21px;color:var(--ink);margin-bottom:10px}
h3.product{font-family:'Open Sans',sans-serif;font-weight:400;font-size:17px;color:#111;margin-bottom:6px}
.btn{display:inline-block;background:linear-gradient(#3fdde6,#14b3bf);border:2px solid #0b6f7a;border-radius:3px;font-family:'Open Sans',sans-serif;font-weight:700;font-size:14px;color:var(--navy);letter-spacing:1px;text-align:center;text-decoration:none}
.btn-view{width:125px;height:26px;line-height:22px;margin-top:2px}
.post{border-bottom:2px solid var(--rule);padding-bottom:10px;margin-bottom:12px}
.post h4{font-size:12px;font-weight:600;color:var(--navy);font-family:'Open Sans',sans-serif}
.post p{font-size:9.5px;line-height:11.5px;color:#222}
.read-more{display:flex;align-items:center;gap:6px;font-size:11.5px;color:#111;margin-bottom:24px}
.quote{position:relative;border:1px solid #cfd5d8;border-radius:8px;padding:14px 12px;height:132px;font-size:11.2px;line-height:14.4px;color:#222}
.quote-tail{position:absolute;left:180px;top:130px}
.client{text-align:right;font-size:11.5px;margin-top:22px;color:#111}

/* footer */
.site-footer{position:absolute;left:0;top:960px;width:1038px;height:186px;background:var(--foot);border-top:3px solid var(--teal)}
.f-col{position:absolute;top:18px}
.f-col h5{font-family:'Yanone Kaffeesatz',sans-serif;font-weight:400;font-size:21px;color:var(--white);margin-bottom:10px}
.f-col li{list-style:none;font-size:10.5px;color:var(--foot-text);line-height:18px}
.f-join p{font-family:'Open Sans',sans-serif;font-size:11px;line-height:14px;color:var(--foot-text);margin-bottom:8px}
.f-input{width:177px;height:20px;background:var(--white);font-size:10.5px;color:#222;padding:3px 8px;margin-bottom:8px;border:1px solid #999}
.btn-submit{width:89px;height:21px;line-height:17px;font-size:13px}
.f-contact p{font-family:'Open Sans',sans-serif;font-size:11px;line-height:14px;color:var(--foot-text);margin-bottom:12px}
.f-contact .label{color:var(--teal-bright)}
.f-contact .link{color:var(--white);text-decoration:underline}
.bottom-bar{position:absolute;left:0;top:1146px;width:1038px;height:54px;background:var(--foot-deep)}
.copyright{position:absolute;left:127px;top:19px;font-family:'Open Sans',sans-serif;font-size:9.5px;color:var(--foot-text)}
.social{position:absolute;left:815px;top:13px;display:flex;gap:10px}
.social span{width:27px;height:27px;border-radius:50%;background:#55585b}
</style>
</head>
<body>

<header class="site-header">
  <div class="brand">
    <div class="brand-dot"></div>
    <div>
      <div class="brand-name">Vantrel Media</div>
      <div class="brand-tag">Specialist Business Consultants</div>
    </div>
  </div>
  <div class="call">Call us: <span>912 346 70815</span></div>
  <div class="search">Search
    <svg width="16" height="15" viewBox="0 0 16 15"><circle cx="6" cy="6" r="4.5" fill="none" stroke="#222" stroke-width="1.6"/><line x1="9.3" y1="9.3" x2="14" y2="14" stroke="#222" stroke-width="2"/></svg>
  </div>
</header>

<nav class="main-nav">
  <ul>
    <li><a href="#">Software Training and Implementation</a></li>
    <li><a href="#">Project Management</a></li>
    <li><a href="#">Business Process Analysis</a></li>
    <li><a href="#">Blog</a></li>
    <li><a href="#">About Us</a></li>
    <li><a href="#">Contact Us</a></li>
  </ul>
</nav>

<section class="hero">
  <div class="hero-art" role="img" aria-label="Illustration of a consultant walking across a tablet beneath a large cloud"></div>
  <div class="hero-title">Vantrel Media</div>
  <div class="hero-sub">Specialist Business Consultants</div>
  <div class="hero-copy">We proviede highly talented technical consultants<br>who are highly trained and experienced with varying<br>degrees of technical and/or management experience.</div>
  <div class="hero-cta">TRY BEFORE YOU BUY</div>
  <a class="consult" href="#">
    <svg width="150" height="72" viewBox="0 0 150 72"><circle cx="80" cy="32" r="32" fill="#ffffff"/><rect x="0" y="38" width="150" height="34" rx="17" fill="#ffffff"/></svg>
    <div class="consult-small">Click Here<br>For</div>
    <div class="consult-big">free! Consultation</div>
  </a>
</section>

<main class="content">
  <div class="col-main">
    <h1 class="welcome">Welcome to Our Website</h1>
    <p>Cloud computing spending is due to account for a third of annual IT expenditure growth by the end of 2013. Every year the range of cloud software systems gets bigger, now including Plumora Accounting, Orbi Apps for Business, Fixnora Job Management Software, Deskwell Suite 365, Projellan Project Manager and many more.</p>
    <p>Signing up for cloud software is only the first part of the process, and then it has to be implemented into your business. That’s where Vantrel Media comes in.</p>
    <p>Formed in 2011, and with a history in cloud computing, implementation and support, we know there’s much more to software implementation and effective business use than the purchase. We can assist by providing an external resource to assist with implementation, as well as getting the right processes post-implementation. Cloud software brings with it a huge array of benefits and efficiencies, but only if resourced and implemented correctly.</p>
    <p>Do you have somebody in your business that you can afford not to work in their role in order to implement? Having seen the negative impact this can have, we are there to help.</p>
    <div class="section-rule"></div>
    <h2 class="section">Featured Software Training</h2>
    <h3 class="product">Orbi Apps</h3>
    <p style="margin-bottom:8px">Cloud based productivity suite that helps you and your team connect and get work done from anywhere on any device. A great alternative to Deskwell Suite which includes word processing, spreadsheets, presentations, emails, chat and more .</p>
    <a class="btn btn-view" href="#">VIEW ALL</a>
  </div>

  <div class="col-divider"></div>

  <aside class="col-side">
    <h2 class="section" style="margin-bottom:26px">Recent Blog Post</h2>
    <div class="post">
      <h4>This is dummy heading</h4>
      <p>Vestibulum laoreet, sem nec egestas commodo, sem enim molestie dui, vel congue augue lectus et mauris.</p>
    </div>
    <div class="post" style="border:none;margin-bottom:6px">
      <h4>This is dummy heading</h4>
      <p>Vestibulum laoreet, sem nec egestas commodo, sem enim molestie dui, vel congue augue lectus et mauris.</p>
    </div>
    <div class="read-more">
      <svg width="11" height="11" viewBox="0 0 11 11"><circle cx="5.5" cy="5.5" r="5.5" fill="#1fc4cf"/><path d="M4 3 L7 5.5 L4 8" fill="none" stroke="#fff" stroke-width="1.5"/></svg>
      Read more
    </div>
    <h2 class="section" style="margin-bottom:18px">Why Our Client Love us</h2>
    <div class="quote">
      “Duis sit amet purus velit. Cum sociis natoque penatibus et magnis dis parturient montes, nascetur ridiculus mus. Quisque bibendum tempor dui, at commodo odio eleifend vitae. Suspendisse ultricies sagittis felis ac consectetur. ”
      <svg class="quote-tail" width="12" height="14" viewBox="0 0 12 14"><path d="M0 0 L1 13 L12 0" fill="#fff" stroke="#cfd5d8"/><rect x="0.5" y="0" width="11" height="2" fill="#fff"/></svg>
    </div>
    <div class="client">Client Name Here</div>
  </aside>
</main>

<footer class="site-footer">
  <div class="f-col" style="left:125px">
    <h5>Quick Links</h5>
    <ul>
      <li>Software Training and Implementation</li>
      <li>Project Management</li>
      <li>Business Process Analysis</li>
      <li>Blog</li>
    </ul>
  </div>
  <div class="f-col" style="left:356px">
    <h5>Information</h5>
    <ul>
      <li>FAQ</li>
      <li>Career</li>
      <li>Privacy Policy</li>
      <li>About Us</li>
    </ul>
  </div>
  <div class="f-col f-join" style="left:510px">
    <h5>Join us</h5>
    <p>Aenean congue hendrerit congue.<br>Quisque id adipiscing felis.</p>
    <div class="f-input">Your name</div>
    <div class="f-input">Email Address</div>
    <a class="btn btn-submit" href="#">SUBMIT</a>
  </div>
  <div class="f-col f-contact" style="left:754px;top:24px">
    <h5>Contact us</h5>
    <p>123 Dummy Street,<br>Dummy State United State.</p>
    <p><span class="label">Email:</span> <span class="link">info@vantrelmedia.com</span></p>
    <p><span class="label">Call us:</span> <span style="color:#fff">912 346 70815</span></p>
  </div>
</footer>

<div class="bottom-bar">
  <div class="copyright">Copyright 2013 vantrelmedia.com All Rights Reserved.</div>
  <div class="social" aria-label="Social links"><span></span><span></span><span></span></div>
</div>

</body>
</html>
```